Mirvane Trinkets
Lucinda Harrow Designs
Mirvane Trinkets -
Creative Brief
Simple
Lucinda Harrow
Jewelry Designer
2719 Quillfern Ln Dallas TX 75294
lucinda@mirvane-example.com
www.mirvane-example.com
Please do a few designs!
Maybe just the logo?

```html
<!DOCTYPE html>
<html lang="en">
<head>
<meta charset="UTF-8">
<title>Mirvane Trinkets – Business Card</title>
<link href="https://fonts.googleapis.com/css2?family=Open+Sans:ital,wght@0,300;0,400;0,700;1,700&display=swap" rel="stylesheet">
<style>
  :root {
    --page-bg: #ece9e4;
    --card-bg: #ffffff;
    --ink-dark: #3a3a3a;
    --ink-mid: #555555;
    --brand-grey: #6b6b6b;
    --brand-teal: #1fb3ac;
    --teal-light: #5fe0d8;
    --teal-deep: #0f8f89;
    --divider: #d9d9d9;
  }
  * { margin: 0; padding: 0; box-sizing: border-box; }
  html, body {
    width: 1200px;
    height: 935px;
    overflow: hidden;
    background: var(--page-bg);
    font-family: "Open Sans", Arial, sans-serif;
  }
  .canvas {
    position: relative;
    width: 1200px;
    height: 935px;
  }
  .business-card {
    position: absolute;
    left: 110px;
    top: 188px;
    width: 980px;
    height: 560px;
    background: var(--card-bg);
    border-radius: 10px 60px 10px 60px;
    overflow: hidden;
    box-shadow: 0 10px 30px rgba(0,0,0,0.18);
  }
  .brand-block {
    position: absolute;
    left: 70px;
    top: 250px;
    display: flex;
    align-items: center;
    gap: 22px;
  }
  .brand-dot {
    width: 54px;
    height: 54px;
    border-radius: 50%;
    background: var(--brand-teal);
  }
  .brand-name {
    font-size: 54px;
    font-weight: 300;
    color: var(--brand-grey);
    letter-spacing: 1px;
    line-height: 1;
  }
  .identity {
    position: absolute;
    right: 70px;
    top: 70px;
    text-align: right;
  }
  .person-name {
    font-size: 32px;
    font-weight: 700;
    color: var(--ink-dark);
  }
  .person-title {
    font-size: 21px;
    font-weight: 700;
    font-style: italic;
    color: var(--ink-mid);
    margin-top: 4px;
  }
  .contact-list {
    position: absolute;
    right: 70px;
    top: 250px;
    text-align: right;
    list-style: none;
    font-size: 20px;
    line-height: 30px;
    color: var(--ink-mid);
  }
  .card-divider {
    position: absolute;
    left: 0;
    right: 0;
    bottom: 74px;
    height: 14px;
    background: linear-gradient(to bottom, #f4f4f4, var(--divider));
  }
  .card-band {
    position: absolute;
    left: 0;
    right: 0;
    bottom: 0;
    height: 74px;
    background: linear-gradient(to bottom, var(--teal-light), var(--brand-teal) 45%, var(--teal-deep));
  }
</style>
</head>
<body>
<main class="canvas">
  <section class="business-card">
    <div class="brand-block">
      <span class="brand-dot"></span>
      <span class="brand-name">Mirvane Trinkets</span>
    </div>

    <header class="identity">
      <h1 class="person-name">Lucinda Harrow</h1>
      <p class="person-title">Jewelry Designer</p>
    </header>

    <ul class="contact-list">
      <li>2719 Quillfern Ln</li>
      <li>Dallas TX 75294</li>
      <li>Phone : 214-555-0187</li>
      <li>Email : lucinda@mirvane-example.com</li>
      <li>Web : www.mirvane-example.com</li>
    </ul>

    <div class="card-divider"></div>
    <div class="card-band"></div>
  </section>
</main>
</body>
</html>
```